Business Card Design for Music Therapy Startup

I began my journey attending the Brantwell College School of Music to become a music educator before changing my degree and graduating with a Bachelor's degree in Music with an Outside Field in Psychology in 2008. From there, I attended Pelham Ridge University where I completed my Bachelor's Equivalency degree in Music Therapy. I became a Board Certified - Music Therapist almost 3 years ago and have since specialized in geriatrics, bereavement and end of life care. I anticipate completing my Master's Degree in Music Therapy in May, 2015, from Quarry Hollow University.

In August of 2014 I completed advanced training in Neurologic Music Therapy (NMT) allowing me to also address speech and language, sensorimotor and cognitive deficits which develop as a result of neurologic injury and disease processes. Parkinson's Disease, Stroke, Traumatic Brain Injury and Dementia are amongst some of the neurologic conditions which may be treated with NMT.

My Philosophy: I strive to provide professional, genuine and compassionate care to all individuals, families and facilities that I serve. I use evidence-based and standardized music-based therapeutic techniques to achieve results which are documented, while complying with privacy regulations. I work with my patients and families to assess the primary goals to be addressed and to establish the most effective treatment plan to facilitate the best results.

Danielle R. Osterby, MT-BC
Neurologic Music Therapist

Willowbrook Music Therapy, LLC

472.906.1543

www.willowbrookmusictherapy.example
willowbrookNMT@mailbox.example

```html
<!DOCTYPE html>
<html lang="en">
<head>
<meta charset="utf-8">
<title>Willowbrook Music Therapy — Business Card</title>
<link rel="stylesheet" href="https://fonts.googleapis.com/css2?family=Marcellus&family=Marcellus+SC&family=Arimo:wght@400&display=swap">
<style>
  :root {
    --page-bg: #d8d3cb;
    --card-bg: #060606;
    --accent-blue: #72a2dc;
    --text-white: #ececec;
    --card-shadow: rgba(0, 0, 0, 0.35);
  }
  * { box-sizing: border-box; margin: 0; padding: 0; }
  html, body {
    width: 1200px;
    height: 800px;
    overflow: hidden;
    background: var(--page-bg);
  }
  .canvas {
    width: 1200px;
    height: 800px;
    display: flex;
    align-items: center;
    justify-content: center;
  }
  .business-card {
    width: 840px;
    height: 480px;
    background: var(--card-bg);
    border-radius: 6px;
    box-shadow: 0 18px 40px var(--card-shadow);
    display: flex;
    flex-direction: column;
    align-items: center;
    justify-content: center;
    text-align: center;
    padding: 40px;
  }
  .brand-mark {
    display: flex;
    align-items: center;
    gap: 14px;
    margin-bottom: 34px;
  }
  .brand-dot {
    width: 14px;
    height: 14px;
    border-radius: 50%;
    background: var(--accent-blue);
  }
  .brand-name {
    font-family: "Marcellus", serif;
    font-weight: 400;
    font-size: 40px;
    color: var(--accent-blue);
    letter-spacing: 0.5px;
  }
  .therapist-name {
    font-family: "Marcellus SC", serif;
    font-size: 34px;
    color: var(--accent-blue);
    letter-spacing: 2px;
  }
  .therapist-title {
    font-family: "Arimo", sans-serif;
    font-size: 19px;
    color: var(--text-white);
    margin-top: 6px;
  }
  .contact-list {
    list-style: none;
    margin-top: 34px;
    font-family: "Arimo", sans-serif;
    font-size: 25px;
    line-height: 1.35;
    color: var(--accent-blue);
  }
</style>
</head>
<body>
  <main class="canvas">
    <section class="business-card">
      <div class="brand-mark">
        <span class="brand-dot"></span>
        <span class="brand-name">Willowbrook Music Therapy, LLC</span>
      </div>
      <h1 class="therapist-name">Danielle R. Osterby</h1>
      <p class="therapist-title">MT-BC Neurologic Music Therapist</p>
      <ul class="contact-list">
        <li class="contact-phone">472.906.1543</li>
        <li class="contact-web">www.willowbrookmusictherapy.example</li>
        <li class="contact-email">willowbrookNMT@mailbox.example</li>
      </ul>
    </section>
  </main>
</body>
</html>
```